letterhead, business card and envelopes

I have the company logo alreday in place...just need a very professional layout for the 3 items listed above

Info for letterhead/business cards and envelopes: Address: Seven Larch Street / Suite B-4 Hampton, NH 03917 (LETTERHEAD, BUSINESS CARDS AND ENVELOPES) tel - 603.284.7719 fax - 603.466.1852 - (LETTERHEAD, BUSINESS CARDS AND ENVELOPES) email: tmv@velbridgesupply.com (business cards only) website: www.velbridgesupply.com (letterhead and business cards only) cell# 603.284.7719 (business card only) Business Card Name: Tobias Merriven. President (business card only)

```html
<!DOCTYPE html>
<html lang="en">
<head>
<meta charset="utf-8">
<title>Velbridge Supply – Stationery Set</title>
<link href="https://fonts.googleapis.com/css2?family=Roboto:wght@400;700&display=swap" rel="stylesheet">
<style>
  :root{
    --navy:#2a2f6b;
    --green:#6aa533;
    --paper:#ffffff;
    --ink:#3a3a3a;
    --muted:#7a7a7a;
    --stage:#e9e9ec;
    --rule:#c9c9cf;
  }
  *{box-sizing:border-box;margin:0;padding:0}
  html,body{width:900px;height:1200px;overflow:hidden}
  body{background:var(--stage);font-family:"Roboto",Arial,sans-serif;color:var(--ink);position:relative}
  .sheet{position:absolute;background:var(--paper);box-shadow:0 2px 6px rgba(0,0,0,.15)}
  .brand{color:var(--navy);font-weight:700;letter-spacing:.04em;white-space:nowrap;line-height:1}
  .band{position:absolute;left:0;display:block}

  /* Letterhead */
  .letterhead{left:171px;top:66px;width:525px;height:759px}
  .letterhead > .brand{position:absolute;top:62px;left:0;right:0;text-align:center;font-size:28px}
  .letterhead > .address{position:absolute;left:26px;top:672px;font-size:9.5px;line-height:15px;color:var(--ink)}
  .letterhead > .band{bottom:0}

  /* Business cards */
  .card{width:270px;height:150px;border:1px solid #ddd;border-radius:6px;overflow:hidden}
  .card-a{left:39px;top:288px}
  .card-b{left:219px;top:348px}
  .card > .brand{position:absolute;left:16px;top:30px;font-size:14px;line-height:16px}
  .card > .person{position:absolute;left:168px;top:22px;width:90px;font-size:7px;line-height:10px;color:var(--muted)}
  .card > .person .name{font-size:9.5px;font-weight:700;color:var(--navy);line-height:13px}
  .card > .contacts{position:absolute;left:168px;top:84px;width:96px;font-size:6px;line-height:9px;color:var(--ink)}
  .card > .street{position:absolute;left:16px;top:126px;font-size:6px;line-height:8px;color:var(--ink)}
  .card > .band{bottom:0}

  /* Envelope */
  .envelope{left:171px;top:876px;width:525px;height:240px}
  .envelope .band-top{top:0}
  .envelope .band-bottom{bottom:0;left:auto;right:0}
  .envelope > .brand{position:absolute;left:24px;top:92px;font-size:22px}
  .envelope > .address{position:absolute;left:24px;top:168px;font-size:7.5px;line-height:11px}
  .envelope > .window{position:absolute;left:300px;top:112px;width:196px;height:62px;border:1px solid var(--rule);border-radius:6px;padding:8px 10px;font-size:8px;color:var(--muted)}
</style>
</head>
<body>

<section class="sheet letterhead" aria-label="Letterhead">
  <div class="brand">VELBRIDGE SUPPLY</div>

  <article class="sheet card card-a" aria-label="Business card">
    <div class="brand">VELBRIDGE<br>SUPPLY</div>
    <div class="person">
      <div class="name">Tobias Merriven</div>
      <div>President</div>
      <div>C : 603.284.7719</div>
    </div>
    <div class="contacts">
      T : 603.284.7719<br>F : 603.466.1852<br>tmv@velbridgesupply.com<br>www.velbridgesupply.com
    </div>
    <div class="street">Seven Larch Street / Suite B-4 · Hampton, NH 03917</div>
    <svg class="band" width="270" height="9" viewBox="0 0 270 9">
      <polygon points="0,3 270,3 270,9 0,9" fill="var(--green)"/>
      <polygon points="0,0 110,0 118,9 0,9" fill="var(--navy)"/>
    </svg>
  </article>

  <article class="sheet card card-b" aria-label="Business card">
    <div class="brand">VELBRIDGE<br>SUPPLY</div>
    <div class="person">
      <div class="name">Tobias Merriven</div>
      <div>President</div>
      <div>C : 603.284.7719</div>
    </div>
    <div class="contacts">
      T : 603.284.7719<br>F : 603.466.1852<br>tmv@velbridgesupply.com<br>www.velbridgesupply.com
    </div>
    <div class="street">Seven Larch Street / Suite B-4 · Hampton, NH 03917</div>
    <svg class="band" width="270" height="9" viewBox="0 0 270 9">
      <polygon points="0,3 270,3 270,9 0,9" fill="var(--green)"/>
      <polygon points="0,0 110,0 118,9 0,9" fill="var(--navy)"/>
    </svg>
  </article>

  <div class="address">
    Seven Larch Street / Suite B-4 · Hampton, NH 03917<br>
    T : 603.284.7719<br>
    F : 603.466.1852<br>
    W : www.velbridgesupply.com
  </div>

  <svg class="band" width="525" height="18" viewBox="0 0 525 18">
    <polygon points="0,6 525,6 525,14 0,14" fill="var(--green)"/>
    <polygon points="430,18 446,2 525,2 525,18" fill="var(--navy)"/>
  </svg>
</section>

<section class="sheet envelope" aria-label="Envelope">
  <svg class="band band-top" width="525" height="26" viewBox="0 0 525 26">
    <polygon points="0,6 525,6 525,16 0,16" fill="var(--green)"/>
    <polygon points="0,0 58,0 76,22 0,22" fill="var(--navy)"/>
  </svg>
  <div class="brand">VELBRIDGE SUPPLY</div>
  <div class="address">
    Seven Larch Street / Suite B-4 · Hampton, NH 03917<br>
    T : 603.284.7719<br>
    F : 603.466.1852<br>
    www.velbridgesupply.com
  </div>
  <div class="window">To:</div>
  <svg class="band band-bottom" width="140" height="14" viewBox="0 0 140 14">
    <polygon points="0,14 12,4 140,4 140,14" fill="var(--green)"/>
    <polygon points="80,14 92,0 140,0 140,14" fill="var(--navy)"/>
  </svg>
</section>

</body>
</html>
```